Recipe mobile app, new flow and design for uploading recipe process

I need a new recipe upload process that's simple, intuitive, and engaging.
The goal is to have a user-friendly and fast flow.
The app is a social recipe library where anyone can upload a recipe after signing up. I currently have a flow, but it's "boring," so I'd like to significantly improve this aspect of the app.
When I create a new recipe, it's immediately saved and labeled as a draft. I'll then need to specify:
- Recipe title
- Cover image (required)
- Number of people (how many people is the recipe for)
- Ingredients (name, quantity, and unit of measurement)
- Recipe explanation (broken down into steps, and I can optionally attach an image to each step)
- Upload
Every change is immediately saved, so you can edit, exit, and resume editing later.
I've attached images of the app and the current upload process.
Thank you.
Low design quality
Good morning everyone,
some of the designs received are fantastic, but please make sure to carefully read the requirement so as not to do extra work.
The requirement is to redesign the flow that a user follows when uploading a recipe to the platform.
We have uploaded the current app screens to give you an idea of what the product looks like, what the colors and style are, but we don’t need a full redesign - only the part mentioned above, while keeping the existing style and colors (we cannot rework the entire theme).
To clarify: if you look at the screens shared in the zip file attached to the project, the focus should be on the screens from 5_.png to 10_.png.
These screens can be redesigned in the most creative way you think, as long as the overall theme remains unchanged.
Thank you for your attention.

```html
<!DOCTYPE html>
<html lang="en">
<head>
<meta charset="utf-8">
<title>Recipe App – New Recipe Full Steps</title>
<link href="https://fonts.googleapis.com/css2?family=Poppins:wght@400;500;600&display=swap" rel="stylesheet">
<style>
:root{
  --orange:#f7931e;
  --green:#27a35a;
  --green-dark:#1f6e45;
  --mint:#33d47e;
  --cream:#fdf7f0;
  --white:#ffffff;
  --ink:#2b2b2b;
  --muted:#9a9a9a;
  --line:#e4e0da;
  --frame:#8c8c8c;
  --pill:#3a3a3a;
}
*{box-sizing:border-box;margin:0;padding:0}
html,body{width:722px;height:1200px;overflow:hidden;background:var(--white)}
body{font-family:"Poppins",sans-serif;color:var(--ink);position:relative}
.board-title{position:absolute;left:33px;top:38px;font-size:19px;font-weight:500;color:var(--orange);letter-spacing:.2px}
.board-sub{position:absolute;left:0;width:722px;top:74px;text-align:center;font-size:11px;font-weight:500;letter-spacing:.3px}

.phone{position:absolute;width:102px;border:1.5px solid var(--frame);border-radius:9px;background:var(--cream);overflow:hidden}
.phone *{position:absolute}
.status{left:0;right:0;top:0;height:14px}
.status .time{left:8px;top:4px;font-size:5px;font-weight:600}
.status svg{right:6px;top:5px}
.appbar{left:0;right:0;top:17px;height:8px}
.appbar .back{left:8px;top:1px;font-size:4px}
.appbar .name{left:16px;top:1.5px;font-size:3px}
.appbar .kebab{right:7px;top:0;font-size:4px;font-weight:600}

.card{left:4px;right:4px;background:var(--white);border-radius:3px}
.lbl{font-size:2.8px;left:5px;white-space:nowrap}
.lbl b{color:var(--orange);font-weight:400;position:static}
.field{left:5px;right:5px;height:6px;border:.5px solid var(--line);border-radius:1.5px;font-size:2.3px;color:var(--muted);padding:1.6px 2px;white-space:nowrap}
.field.filled{color:var(--ink)}
.btn-o{height:6px;border:.6px solid var(--green);color:var(--green);border-radius:4px;font-size:2.3px;text-align:center;line-height:5px;white-space:nowrap}
.btn-s{height:7px;background:var(--green);color:var(--white);border-radius:1.5px;font-size:2.3px;text-align:center;line-height:7px;white-space:nowrap}
.btn-rect{height:7px;border:.6px solid var(--green);color:var(--green);border-radius:1.5px;font-size:2.3px;text-align:center;line-height:6px;white-space:nowrap;background:var(--white)}
.chip{height:5px;background:var(--green);color:var(--white);border-radius:3px;font-size:2.2px;text-align:center;line-height:5px;width:12px}
.chip.ghost{background:transparent;color:var(--muted);border:none}
.cam{width:12px;height:12px;border-radius:50%;background:var(--green)}
.cam svg{left:3px;top:3px}

.swipe{height:16px;width:52px;left:24px;background:var(--pill);border-radius:8px}
.swipe .knob{left:1.5px;top:1.5px;width:13px;height:13px;border-radius:50%;background:var(--green);color:var(--white);font-size:6px;text-align:center;line-height:12px;font-weight:600}
.swipe .chev{left:20px;top:3px;font-size:6px;color:var(--white);letter-spacing:-1px;font-weight:600}
.homebar{width:36px;height:1.2px;background:var(--ink);left:32px;border-radius:1px}

.row{left:5px;right:5px;height:4px;font-size:2.3px;color:var(--muted);border-bottom:.4px solid var(--line)}
.row .q{left:58px;top:0;width:9px;height:3px;border:.4px solid var(--line);font-size:2px;text-align:center}
.row .u{left:73px;top:0;font-size:2px;color:var(--ink)}
.sec-title{left:5px;right:5px;height:6px;border:.5px solid var(--line);border-radius:1.5px;font-size:2.3px;padding:1.6px 2px}

.thumb{border-radius:50%}
.photo{background:linear-gradient(135deg,#e9ddd6,#6b3a34 55%,#2d1a18)}
.step-title{height:6px;border:.5px solid var(--line);border-radius:1.5px;font-size:2.3px;color:var(--green);padding:1.6px 2px;white-space:nowrap}
.step-text{left:5px;right:5px;border:.5px solid var(--line);border-radius:1.5px;font-size:2px;color:var(--muted);padding:1.5px 2px;line-height:2.8px}
.step-text span{position:static;display:block}

.overlay{left:0;right:0;top:0;bottom:0;background:rgba(60,60,60,.62)}
.modal{background:var(--mint);border-radius:3px;color:var(--white);text-align:center}

.detail .hdr{left:0;right:0;top:0;height:50px;background:var(--green-dark)}
.tiny{font-size:2.2px;color:var(--muted);white-space:nowrap}
.tiny.dark{color:var(--ink)}
.tiny.green{color:var(--green)}
.h{font-size:3px;font-weight:500;white-space:nowrap}
.dish{width:10px;height:10px;border-radius:3px}
</style>
</head>
<body>

<div class="board-title">RECIPE APP SCREEN</div>
<div class="board-sub">NEW RECIPE FULL STEPS SCREEN</div>

<!-- ROW 1 : Phone 1 – empty name & image -->
<div class="phone" style="left:32px;top:104px;height:218px">
  <div class="status"><span class="time">9:14</span>
    <svg width="18" height="5" viewBox="0 0 18 5"><rect x="0" y="3" width="1" height="2" fill="#2b2b2b"/><rect x="1.6" y="2" width="1" height="3" fill="#2b2b2b"/><rect x="3.2" y="0.5" width="1" height="4.5" fill="#2b2b2b"/><path d="M6 2.2a3.5 3.5 0 0 1 5 0M7 3.3a2 2 0 0 1 3 0" stroke="#2b2b2b" stroke-width=".7" fill="none"/><rect x="12.5" y="1" width="5" height="3" rx=".8" fill="none" stroke="#2b2b2b" stroke-width=".6"/><rect x="13.2" y="1.6" width="3.6" height="1.8" fill="#2b2b2b"/></svg></div>
  <div class="appbar"><span class="back">←</span><span class="name">New Recipes</span><span class="kebab">⋮</span></div>
  <div class="card" style="top:30px;height:92px">
    <span class="lbl" style="top:5px">Name Of Your Recipe<b>*</b></span>
    <div class="field" style="top:10px">Enter Name</div>
    <span class="lbl" style="top:24px">Upload Your Recipe Image<b>*</b></span>
    <div class="cam" style="left:41px;top:44px"><svg width="6" height="6" viewBox="0 0 6 6"><rect x=".3" y="1.3" width="5.4" height="4" rx=".8" fill="#fff"/><circle cx="3" cy="3.3" r="1.1" fill="#27a35a"/><rect x="2" y=".6" width="2" height="1" fill="#fff"/></svg></div>
    <div class="btn-o" style="left:18px;top:79px;width:19px">Upload Gallery</div>
    <div class="btn-o" style="left:41px;top:79px;width:19px">Take A Photo</div>
  </div>
  <div class="card" style="top:126px;height:40px">
    <span class="lbl" style="top:5px;left:9px">Total No Of Serves<b>*</b></span>
    <div class="thumb" style="left:4px;top:5px;width:3.5px;height:3.5px;background:var(--orange)"></div>
    <div class="field" style="top:12px">0</div>
    <div class="btn-o" style="right:5px;top:28px;width:12px">Save</div>
  </div>
  <div class="swipe" style="top:183px"><span class="knob">›</span><span class="chev">› › ›</span></div>
  <div class="homebar" style="top:203px"></div>
</div>

<!-- Phone 2 – filled name & image -->
<div class="phone" style="left:143px;top:104px;height:218px">
  <div class="status"><span class="time">9:14</span>
    <svg width="18" height="5" viewBox="0 0 18 5"><rect x="0" y="3" width="1" height="2" fill="#2b2b2b"/><rect x="1.6" y="2" width="1" height="3" fill="#2b2b2b"/><rect x="3.2" y="0.5" width="1" height="4.5" fill="#2b2b2b"/><path d="M6 2.2a3.5 3.5 0 0 1 5 0M7 3.3a2 2 0 0 1 3 0" stroke="#2b2b2b" stroke-width=".7" fill="none"/><rect x="12.5" y="1" width="5" height="3" rx=".8" fill="none" stroke="#2b2b2b" stroke-width=".6"/><rect x="13.2" y="1.6" width="3.6" height="1.8" fill="#2b2b2b"/></svg></div>
  <div class="appbar"><span class="back">←</span><span class="name">New Recipes</span><span class="kebab">⋮</span></div>
  <div class="card" style="top:30px;height:92px">
    <span class="lbl" style="top:5px">Name Of Your Recipe<b>*</b></span>
    <div class="field filled" style="top:10px">Black Forest Cake</div>
    <span class="lbl" style="top:24px">Upload Your Recipe Image<b>*</b></span>
    <div class="thumb photo" role="img" aria-label="Black forest cake cover photo" style="left:36px;top:38px;width:24px;height:24px"></div>
    <div class="btn-o" style="left:18px;top:79px;width:19px">Upload Gallery</div>
    <div class="btn-o" style="left:41px;top:79px;width:19px">Take A Photo</div>
  </div>
  <div class="card" style="top:126px;height:40px">
    <span class="lbl" style="top:5px;left:9px">Total No Of Serves<b>*</b></span>
    <div class="thumb" style="left:4px;top:5px;width:3.5px;height:3.5px;background:var(--orange)"></div>
    <div class="field filled" style="top:12px">10-12</div>
    <div class="btn-o" style="right:5px;top:28px;width:12px">Save</div>
  </div>
  <div class="swipe" style="top:183px"><span class="knob">›</span><span class="chev">› › ›</span></div>
  <div class="homebar" style="top:203px"></div>
</div>

<!-- Phone 3 – ingredients empty -->
<div class="phone" style="left:254px;top:104px;height:218px">
  <div class="status"><span class="time">9:14</span>
    <svg width="18" height="5" viewBox="0 0 18 5"><rect x="0" y="3" width="1" height="2" fill="#2b2b2b"/><rect x="1.6" y="2" width="1" height="3" fill="#2b2b2b"/><rect x="3.2" y="0.5" width="1" height="4.5" fill="#2b2b2b"/><path d="M6 2.2a3.5 3.5 0 0 1 5 0M7 3.3a2 2 0 0 1 3 0" stroke="#2b2b2b" stroke-width=".7" fill="none"/><rect x="12.5" y="1" width="5" height="3" rx=".8" fill="none" stroke="#2b2b2b" stroke-width=".6"/><rect x="13.2" y="1.6" width="3.6" height="1.8" fill="#2b2b2b"/></svg></div>
  <div class="appbar"><span class="back">←</span><span class="name">New Recipes</span><span class="kebab">⋮</span></div>
  <div class="card" style="top:30px;height:124px">
    <span class="lbl" style="top:5px">Ingredients<b>*</b></span>
    <div class="field" style="top:11px">Enter Your Ingredient Name</div>
    <div class="row" style="top:22px">Item Name1<span class="q">00</span><span class="u">gm ▾</span></div>
    <div class="row" style="top:30px">Item Name2<span class="q">00</span><span class="u">gm ▾</span></div>
    <div class="row" style="top:38px">Item Name3<span class="q">00</span><span class="u">tsp ▾</span></div>
    <div class="row" style="top:46px">Item Name4<span class="q">00</span><span class="u">tsp ▾</span></div>
    <div class="row" style="top:54px">Item Name5<span class="q">00</span><span class="u">tsp ▾</span></div>
    <div class="row" style="top:62px">Item Name6<span class="q">00</span><span class="u">gm ▾</span></div>
    <div class="row" style="top:70px">Item Name7<span class="q">00</span><span class="u">ml ▾</span></div>
    <div class="row" style="top:78px">Item Name8<span class="q">00</span><span class="u">ml ▾</span></div>
    <div class="row" style="top:86px">Item Name9<span class="q">00</span><span class="u">tsp ▾</span></div>
    <div class="row" style="top:94px">Item Name10<span class="q">00</span><span class="u">ml ▾</span></div>
    <div class="btn-o" style="right:5px;top:112px;width:12px">Add</div>
  </div>
  <div class="card" style="top:159px;height:10px;border:.5px solid var(--line)">
    <span class="tiny dark" style="left:0;right:0;top:3px;text-align:center">Add Next Section</span>
  </div>
  <div class="swipe" style="top:183px"><span class="knob">›</span><span class="chev">› › ›</span></div>
  <div class="homebar" style="top:203px"></div>
</div>

<!-- Phone 4 – ingredients filled, tall -->
<div class="phone" style="left:365px;top:104px;height:371px">
  <div class="status"><span class="time">9:14</span>
    <svg width="18" height="5" viewBox="0 0 18 5"><rect x="0" y="3" width="1" height="2" fill="#2b2b2b"/><rect x="1.6" y="2" width="1" height="3" fill="#2b2b2b"/><rect x="3.2" y="0.5" width="1" height="4.5" fill="#2b2b2b"/><path d="M6 2.2a3.5 3.5 0 0 1 5 0M7 3.3a2 2 0 0 1 3 0" stroke="#2b2b2b" stroke-width=".7" fill="none"/><rect x="12.5" y="1" width="5" height="3" rx=".8" fill="none" stroke="#2b2b2b" stroke-width=".6"/><rect x="13.2" y="1.6" width="3.6" height="1.8" fill="#2b2b2b"/></svg></div>
  <div class="appbar"><span class="back">←</span><span class="name">New Recipes</span><span class="kebab">⋮</span></div>
  <div class="card" style="top:30px;height:125px">
    <span class="lbl" style="top:5px">Ingredients<b>*</b></span>
    <div class="sec-title" style="top:12px">For The Chocolate Sponge Cake</div>
    <div class="row" style="top:23px">All-Purpose Flour<span class="q">200</span><span class="u">gm ▾</span></div>
    <div class="row" style="top:31px">Cocoa Powder<span class="q">50</span><span class="u">gm ▾</span></div>
    <div class="row" style="top:39px">Baking Powder<span class="q">1</span><span class="u">tsp ▾</span></div>
    <div class="row" style="top:47px">Baking Soda<span class="q">1/2</span><span class="u">tsp ▾</span></div>
    <div class="row" style="top:55px">Salt<span class="q">1/4</span><span class="u">tsp ▾</span></div>
    <div class="row" style="top:63px">Sugar<span class="q">150</span><span class="u">gm ▾</span></div>
    <div class="row" style="top:71px">Milk<span class="q">120</span><span class="u">ml ▾</span></div>
    <div class="row" style="top:79px">Vegetable Oil<span class="q">60</span><span class="u">ml ▾</span></div>
    <div class="row" style="top:87px">Vanilla Extract<span class="q">1</span><span class="u">tsp ▾</span></div>
    <div class="row" style="top:95px">Hot Water<span class="q">120</span><span class="u">ml ▾</span></div>
    <div class="btn-o" style="right:5px;top:112px;width:12px">Add</div>
  </div>
  <div class="card" style="top:163px;height:52px">
    <span class="tiny dark" style="left:5px;top:4px">For The Cherry Filling</span>
    <div class="row" style="top:13px">Canned Sour Cherries<span class="q">400</span><span class="u">gm ▾</span></div>
    <div class="row" style="top:21px">Cornstarch<span class="q">2</span><span class="u">tbsp ▾</span></div>
    <div class="row" style="top:29px">Sugar<span class="q">2</span><span class="u">tbsp ▾</span></div>
    <div class="btn-o" style="right:5px;top:41px;width:12px">Add</div>
  </div>
  <div class="card" style="top:221px;height:54px">
    <div class="field" style="top:4px">Enter Your Section Name</div>
    <div class="row" style="top:15px">Heavy Whipping Cream<span class="q">300</span><span class="u">ml ▾</span></div>
    <div class="row" style="top:23px">Powdered Sugar<span class="q">80</span><span class="u">gm ▾</span></div>
    <div class="row" style="top:31px">Vanilla Extract<span class="q">1</span><span class="u">tsp ▾</span></div>
    <div class="btn-o" style="right:5px;top:43px;width:12px">Add</div>
  </div>
  <div class="card" style="top:281px;height:46px">
    <span class="tiny dark" style="left:5px;top:4px">For Decoration</span>
    <div class="row" style="top:13px">Chocolate Shavings<span class="q">100</span><span class="u">ml ▾</span></div>
    <div class="row" style="top:21px">Maraschino Cherries<span class="q">10-12</span><span class="u">pcs ▾</span></div>
    <div class="btn-o" style="right:5px;top:34px;width:12px">Add</div>
  </div>
  <div class="card" style="top:331px;height:10px;border:.5px solid var(--line)">
    <span class="tiny dark" style="left:0;right:0;top:3px;text-align:center">Add Next Section</span>
  </div>
  <div class="swipe" style="top:344px"><span class="knob">›</span><span class="chev">› › ›</span></div>
  <div class="homebar" style="top:364px"></div>
</div>

<!-- Phone 5 – recipe steps choice / docs -->
<div class="phone" style="left:476px;top:104px;height:218px">
  <div class="status"><span class="time">9:14</span>
    <svg width="18" height="5" viewBox="0 0 18 5"><rect x="0" y="3" width="1" height="2" fill="#2b2b2b"/><rect x="1.6" y="2" width="1" height="3" fill="#2b2b2b"/><rect x="3.2" y="0.5" width="1" height="4.5" fill="#2b2b2b"/><path d="M6 2.2a3.5 3.5 0 0 1 5 0M7 3.3a2 2 0 0 1 3 0" stroke="#2b2b2b" stroke-width=".7" fill="none"/><rect x="12.5" y="1" width="5" height="3" rx=".8" fill="none" stroke="#2b2b2b" stroke-width=".6"/><rect x="13.2" y="1.6" width="3.6" height="1.8" fill="#2b2b2b"/></svg></div>
  <div class="appbar"><span class="back">←</span><span class="name">New Recipes</span><span class="kebab">⋮</span></div>
  <div class="card" style="top:30px;height:52px">
    <span class="lbl" style="top:5px">Upload Your Recipe Steps<b>*</b></span>
    <div class="btn-rect" style="left:10px;right:10px;top:13px;color:var(--ink);border-color:var(--line)">AutoChef Recipe</div>
    <span class="tiny green" style="left:0;right:0;top:24px;text-align:center">Or</span>
    <div class="btn-rect" style="left:10px;right:10px;top:29px;color:var(--ink);border-color:var(--line)">Handcrafted Recipe</div>
  </div>
  <div class="card" style="top:88px;height:64px">
    <span class="lbl" style="top:5px">Upload Docs<b>*</b></span>
    <svg style="left:44px;top:20px" width="10" height="13" viewBox="0 0 10 13"><path d="M0 1a1 1 0 0 1 1-1h5.5L10 3.5V12a1 1 0 0 1-1 1H1a1 1 0 0 1-1-1z" fill="#27a35a"/><rect x="2.5" y="6" width="5" height=".8" fill="#fff"/><rect x="2.5" y="8" width="5" height=".8" fill="#fff"/><rect x="2.5" y="10" width="5" height=".8" fill="#fff"/></svg>
    <div class="btn-rect" style="left:10px;right:10px;top:50px">Upload Your Docs</div>
  </div>
  <div class="btn-rect" style="left:10px;right:10px;top:168px;height:8px;line-height:7px">Update</div>
</div>

<!-- Phone 6 – AutoChef selected, uploading -->
<div class="phone" style="left:588px;top:104px;height:218px">
  <div class="status"><span class="time">9:14</span>
    <svg width="18" height="5" viewBox="0 0 18 5"><rect x="0" y="3" width="1" height="2" fill="#2b2b2b"/><rect x="1.6" y="2" width="1" height="3" fill="#2b2b2b"/><rect x="3.2" y="0.5" width="1" height="4.5" fill="#2b2b2b"/><path d="M6 2.2a3.5 3.5 0 0 1 5 0M7 3.3a2 2 0 0 1 3 0" stroke="#2b2b2b" stroke-width=".7" fill="none"/><rect x="12.5" y="1" width="5" height="3" rx=".8" fill="none" stroke="#2b2b2b" stroke-width=".6"/><rect x="13.2" y="1.6" width="3.6" height="1.8" fill="#2b2b2b"/></svg></div>
  <div class="appbar"><span class="back">←</span><span class="name">New Recipes</span><span class="kebab">⋮</span></div>
  <div class="card" style="top:30px;height:52px">
    <span class="lbl" style="top:5px">Upload Your Recipe Steps<b>*</b></span>
    <div class="btn-s" style="left:10px;right:10px;top:13px;height:8px;line-height:8px">AutoChef Recipe</div>
    <span class="tiny green" style="left:0;right:0;top:24px;text-align:center">Or</span>
    <div class="btn-rect" style="left:10px;right:10px;top:29px;color:var(--ink);border-color:var(--line)">Handcrafted Recipe</div>
  </div>
  <div class="card" style="top:88px;height:64px">
    <span class="lbl" style="top:5px">Upload Docs<b>*</b></span>
    <svg style="left:37px;top:15px" width="24" height="24" viewBox="0 0 24 24"><circle cx="12" cy="12" r="11" fill="none" stroke="#e4e0da" stroke-width=".8"/><path d="M12 1a11 11 0 1 1-9.5 16.5" fill="none" stroke="#27a35a" stroke-width="1"/><path d="M7.5 6.5a.8.8 0 0 1 .8-.8h5L17 9.3v8a.8.8 0 0 1-.8.8H8.3a.8.8 0 0 1-.8-.8z" fill="#27a35a"/><rect x="9.5" y="11" width="5" height=".8" fill="#fff"/><rect x="9.5" y="13" width="5" height=".8" fill="#fff"/><rect x="9.5" y="15" width="5" height=".8" fill="#fff"/></svg>
    <div class="btn-rect" style="left:10px;right:10px;top:50px">Upload Your Docs</div>
  </div>
  <div class="btn-rect" style="left:10px;right:10px;top:168px;height:8px;line-height:7px">Update</div>
</div>

<!-- ROW 2 : Phone 7 – handcrafted empty step -->
<div class="phone" style="left:32px;top:526px;height:217px">
  <div class="status"><span class="time">9:14</span>
    <svg width="18" height="5" viewBox="0 0 18 5"><rect x="0" y="3" width="1" height="2" fill="#2b2b2b"/><rect x="1.6" y="2" width="1" height="3" fill="#2b2b2b"/><rect x="3.2" y="0.5" width="1" height="4.5" fill="#2b2b2b"/><path d="M6 2.2a3.5 3.5 0 0 1 5 0M7 3.3a2 2 0 0 1 3 0" stroke="#2b2b2b" stroke-width=".7" fill="none"/><rect x="12.5" y="1" width="5" height="3" rx=".8" fill="none" stroke="#2b2b2b" stroke-width=".6"/><rect x="13.2" y="1.6" width="3.6" height="1.8" fill="#2b2b2b"/></svg></div>
  <div class="appbar"><span class="back">←</span><span class="name">New Recipes</span><span class="kebab">⋮</span></div>
  <div class="card" style="top:30px;height:54px">
    <span class="lbl" style="top:5px">Upload Your Recipe Steps<b>*</b></span>
    <div class="btn-rect" style="left:10px;right:10px;top:13px;color:var(--ink);border-color:var(--line)">AutoChef Recipe</div>
    <span class="tiny green" style="left:0;right:0;top:24px;text-align:center">Or</span>
    <div class="btn-s" style="left:10px;right:10px;top:30px;height:8px;line-height:8px">Handcrafted Recipe</div>
  </div>
  <div class="card" style="top:90px;height:92px">
    <span class="lbl" style="top:5px">Recipe Steps</span>
    <svg style="left:12px;top:18px" width="6" height="5" viewBox="0 0 6 5"><rect y=".8" width="6" height="4.2" rx=".8" fill="#27a35a"/><circle cx="3" cy="3" r="1.1" fill="#fff"/></svg>
    <div class="field" style="left:30px;top:17px">Enter Your Steps Name</div>
    <div class="field" style="top:31px;height:34px">Enter your details</div>
    <span class="tiny" style="right:7px;top:61px;font-size:1.9px">0/500</span>
    <div class="field" style="top:70px;height:8px;text-align:center;color:var(--ink);padding-top:2.5px">Add Next Steps</div>
  </div>
  <div class="btn-rect" style="left:10px;right:10px;top:190px;height:8px;line-height:7px">Update</div>
</div>

<!-- Phone 8 – handcrafted steps filled, tall -->
<div class="phone" style="left:143px;top:526px;height:507px">
  <div class="status"><span class="time">9:14</span>
    <svg width="18" height="5" viewBox="0 0 18 5"><rect x="0" y="3" width="1" height="2" fill="#2b2b2b"/><rect x="1.6" y="2" width="1" height="3" fill="#2b2b2b"/><rect x="3.2" y="0.5" width="1" height="4.5" fill="#2b2b2b"/><path d="M6 2.2a3.5 3.5 0 0 1 5 0M7 3.3a2 2 0 0 1 3 0" stroke="#2b2b2b" stroke-width=".7" fill="none"/><rect x="12.5" y="1" width="5" height="3" rx=".8" fill="none" stroke="#2b2b2b" stroke-width=".6"/><rect x="13.2" y="1.6" width="3.6" height="1.8" fill="#2b2b2b"/></svg></div>
  <div class="appbar"><span class="back">←</span><span class="name">New Recipes</span><span class="kebab">⋮</span></div>
  <div class="card" style="top:30px;height:54px">
    <span class="lbl" style="top:5px">Upload Your Recipe Steps<b>*</b></span>
    <div class="btn-rect" style="left:10px;right:10px;top:13px;color:var(--ink);border-color:var(--line)">AutoChef Recipe</div>
    <span class="tiny green" style="left:0;right:0;top:24px;text-align:center">Or</span>
    <div class="btn-s" style="left:10px;right:10px;top:30px;height:8px;line-height:8px">Handcrafted Recipe</div>
  </div>
  <div class="card" style="top:90px;height:385px">
    <span class="lbl" style="top:5px">Recipe Steps</span>

    <div class="thumb photo" role="img" aria-label="Chocolate sponge step photo" style="left:4px;top:13px;width:12px;height:12px"></div>
    <div class="step-title" style="left:30px;right:5px;top:15px">Step 1: Prepare The Chocolate Sponge</div>
    <div class="step-text" style="top:29px;height:36px"><span>1. Preheat oven to 175°C, grease two round cake pans.</span><span>2. In a bowl, sift flour, cocoa, baking powder, soda and salt.</span><span>3. Beat eggs and sugar until light, add milk, oil, vanilla.</span><span>4. Fold in dry mix, then add hot water and stir well.</span><span>5. Pour into pans and bake 30-35 minutes, then cool.</span></div>
    <span class="chip ghost" style="left:64px;top:69px">Delete</span><span class="chip" style="left:78px;top:69px">Edit</span>

    <div class="thumb" role="img" aria-label="Cherry filling step photo" style="left:4px;top:80px;width:12px;height:12px;background:linear-gradient(135deg,#f1e4dc,#b3262d)"></div>
    <div class="step-title" style="left:30px;right:5px;top:82px">Step 2: Make The Cherry Filling</div>
    <div class="step-text" style="top:96px;height:17px"><span>1. In a saucepan, heat drained cherries with syrup.</span><span>2. Mix cornstarch with water, add to pan and stir.</span><span>3. Cook until thickened, add cherries and cool.</span></div>
    <span class="chip ghost" style="left:64px;top:117px">Delete</span><span class="chip" style="left:78px;top:117px">Edit</span>

    <div class="thumb" role="img" aria-label="Whipped cream step photo" style="left:4px;top:127px;width:12px;height:12px;background:linear-gradient(135deg,#f3e3d3,#8a4a2a)"></div>
    <div class="step-title" style="left:30px;right:5px;top:129px">Step 3: Whip The Cream</div>
    <div class="step-text" style="top:143px;height:17px"><span>1. Chill mixing bowl and beaters first.</span><span>2. Beat cream to soft peaks, add sugar and vanilla.</span><span>3. Keep whipping until stiff peaks form, then chill.</span></div>
    <span class="chip ghost" style="left:64px;top:164px">Delete</span><span class="chip" style="left:78px;top:164px">Edit</span>

    <div class="thumb" role="img" aria-label="Assembling cake step photo" style="left:4px;top:173px;width:12px;height:12px;background:linear-gradient(135deg,#d9cfc9,#3a2a28)"></div>
    <div class="step-title" style="left:30px;right:5px;top:175px">Step 4: Assemble The Cake</div>
    <div class="step-text" style="top:189px;height:17px"><span>1. Slice cakes into two layers and add syrup.</span><span>2. Place one layer on a plate, brush with syrup.</span><span>3. Spread cream, then cherries, and repeat layers.</span></div>
    <span class="chip ghost" style="left:64px;top:210px">Delete</span><span class="chip" style="left:78px;top:210px">Edit</span>

    <div class="thumb" role="img" aria-label="Decorated cake step photo" style="left:4px;top:219px;width:12px;height:12px;background:linear-gradient(135deg,#f6dfe0,#c06070)"></div>
    <div class="step-title" style="left:30px;right:5px;top:221px">Step 5: Frost And Decorate</div>
    <div class="step-text" style="top:235px;height:14px"><span>1. Cover the cake with whipped cream.</span><span>2. Press chocolate shavings onto the sides.</span><span>3. Top with cream swirls and cherries.</span></div>
    <span class="chip ghost" style="left:64px;top:253px">Delete</span><span class="chip" style="left:78px;top:253px">Edit</span>

    <div class="field" style="top:266px;height:9px;text-align:center;color:var(--ink);padding-top:3px">Add Next Steps</div>
  </div>
  <div class="btn-rect" style="left:10px;right:10px;top:384px;height:9px;line-height:8px">Update</div>
</div>

<!-- Phone 9 – success modal -->
<div class="phone" style="left:255px;top:526px;height:217px">
  <div class="status"><span class="time">9:14</span>
    <svg width="18" height="5" viewBox="0 0 18 5"><rect x="0" y="3" width="1" height="2" fill="#2b2b2b"/><rect x="1.6" y="2" width="1" height="3" fill="#2b2b2b"/><rect x="3.2" y="0.5" width="1" height="4.5" fill="#2b2b2b"/><path d="M6 2.2a3.5 3.5 0 0 1 5 0M7 3.3a2 2 0 0 1 3 0" stroke="#2b2b2b" stroke-width=".7" fill="none"/><rect x="12.5" y="1" width="5" height="3" rx=".8" fill="none" stroke="#2b2b2b" stroke-width=".6"/><rect x="13.2" y="1.6" width="3.6" height="1.8" fill="#2b2b2b"/></svg></div>
  <div class="appbar"><span class="back">←</span><span class="name">New Recipes</span><span class="kebab">⋮</span></div>
  <div class="card" style="top:30px;height:92px">
    <span class="lbl" style="top:5px">Name Of Your Recipe<b>*</b></span>
    <div class="field filled" style="top:10px">Black Forest Cake</div>
    <span class="lbl" style="top:24px">Upload Your Recipe Image<b>*</b></span>
  </div>
  <div class="card" style="top:126px;height:40px">
    <div class="field filled" style="top:12px">10-12</div>
    <div class="btn-o" style="right:5px;top:28px;width:12px">Save</div>
  </div>
  <div class="card" style="top:172px;height:60px">
    <span class="lbl" style="top:4px">Ingredients<b>*</b></span>
    <div class="sec-title" style="top:12px">For The Chocolate Sponge Cake</div>
    <div class="row" style="top:23px">All-Purpose Flour<span class="q">200</span><span class="u">gm ▾</span></div>
  </div>
  <div class="overlay"></div>
  <div class="modal" style="left:5px;right:5px;top:64px;height:72px">
    <svg style="left:38px;top:10px" width="18" height="18" viewBox="0 0 18 18"><circle cx="9" cy="9" r="8" fill="none" stroke="#1f6e45" stroke-width="1"/><circle cx="9" cy="9" r="5" fill="none" stroke="#1f6e45" stroke-width="1"/><circle cx="9" cy="9" r="2" fill="#1f6e45"/><path d="M9 9l6-6M13 2h2.5v2.5" stroke="#1f6e45" stroke-width="1" fill="none"/></svg>
    <span class="h" style="left:0;right:0;top:35px;font-size:3.6px;font-weight:600">Recipe Uploaded Successfully</span>
    <span style="left:0;right:0;top:45px;font-size:3.1px;line-height:4.6px">Your Black Forest Cake Recipe<br>Has Been Uploaded Successfully</span>
  </div>
</div>

<!-- Phone 10 – published recipe detail -->
<div class="phone detail" style="left:367px;top:526px;height:606px;background:var(--white)">
  <div class="hdr"></div>
  <div class="status"><span class="time" style="color:#fff">9:14</span>
    <svg width="18" height="5" viewBox="0 0 18 5"><rect x="0" y="3" width="1" height="2" fill="#fff"/><rect x="1.6" y="2" width="1" height="3" fill="#fff"/><rect x="3.2" y="0.5" width="1" height="4.5" fill="#fff"/><path d="M6 2.2a3.5 3.5 0 0 1 5 0M7 3.3a2 2 0 0 1 3 0" stroke="#fff" stroke-width=".7" fill="none"/><rect x="12.5" y="1" width="5" height="3" rx=".8" fill="none" stroke="#fff" stroke-width=".6"/><rect x="13.2" y="1.6" width="3.6" height="1.8" fill="#fff"/></svg></div>
  <span class="tiny" style="left:8px;top:21px;color:#cfe6d8">◁</span>
  <span class="tiny" style="left:17px;top:20px;color:#cfe6d8;line-height:3px">12 Maple Row<br>Deliver here</span>
  <span class="tiny" style="right:8px;top:21px;color:#cfe6d8">♡ ♢ ⚙</span>
  <div style="left:5px;top:34px;width:74px;height:8px;border-radius:4px;background:#5b8a6f"></div>
  <span class="tiny" style="left:15px;top:36.5px;color:#e5f1ea">Search your recipe</span>
  <div style="left:48px;top:35px;width:6px;height:6px;border-radius:50%;background:#222;color:#fff;font-size:4px;text-align:center;line-height:6px">×</div>
  <div style="left:82px;top:34px;width:14px;height:8px;border-radius:2px;background:#8fb9a0"></div>

  <div style="left:3px;right:3px;top:52px;height:264px;background:var(--cream);border-radius:3px"></div>
  <div role="img" aria-label="Black forest cake hero photo" style="left:7px;top:57px;width:86px;height:49px;border-radius:2px;background:linear-gradient(160deg,#d6d3d2,#4b2d2c 55%,#231616)"></div>
  <span class="tiny green" style="left:8px;top:110px">4.5 ★</span>
  <span class="tiny dark" style="right:8px;top:109px">♡ ↗ ⋮</span>
  <span class="h" style="left:8px;top:116px;font-size:4px">Black Forest Cake</span>
  <div style="left:8px;top:124px;width:12px;height:1.8px;background:var(--green);border-radius:1px"></div>
  <span class="tiny dark" style="left:22px;top:123px;font-size:1.9px">Highly Recommend</span>
  <span class="tiny" style="left:8px;top:128px;font-size:1.9px;line-height:2.8px;white-space:normal;width:84px">Black Forest Cake is a classic German dessert made with rich chocolate sponge, fresh whipped cream, cherry filling and chocolate shavings, offering a decadent, festive delight.</span>
  <span class="tiny dark" style="left:8px;top:141px;font-size:1.9px">Italian Style · 500g <span style="position:static;color:var(--orange)">Read More</span></span>
  <div class="thumb" role="img" aria-label="Chef profile photo" style="left:8px;top:149px;width:9px;height:9px;background:#7a6e66"></div>
  <span class="tiny dark" style="left:20px;top:150px">Leo Barton</span>
  <span class="tiny green" style="left:20px;top:153px;font-size:1.8px">★★★★★</span>
  <span class="chip" style="left:78px;top:151px;width:14px;height:5px">Follow</span>

  <div style="left:3px;right:3px;top:164px;height:92px;background:var(--white);border-radius:2px;border:.4px solid var(--line)"></div>
  <span class="h" style="left:8px;top:167px;font-size:2.7px">Servings</span>
  <span class="tiny" style="left:8px;top:171px;font-size:1.9px">Total serves: 10-12 people</span>
  <span class="tiny" style="right:9px;top:168px;color:var(--orange);font-size:1.9px">Saved</span>
  <span class="h" style="left:8px;top:177px;font-size:2.7px">Ingredients</span>
  <span class="tiny dark" style="left:8px;top:182px;font-size:1.9px">For the Chocolate Sponge Cake</span>
  <span class="tiny" style="left:8px;top:185px;font-size:1.8px;line-height:2.6px">All-purpose flour – 200 g, Cocoa powder – 50 g<br>Baking powder – 1 tsp, Baking soda – ½ tsp, Salt<br>Sugar – 150 g, Milk – 120 ml, Vegetable oil – 60 ml<br>Vanilla extract – 1 tsp, Hot water – 120 ml</span>
  <span class="tiny dark" style="left:8px;top:197px;font-size:1.9px">For the Cherry Filling</span>
  <span class="tiny" style="left:8px;top:200px;font-size:1.8px;line-height:2.6px">Canned sour cherries – 400 g, reserve syrup<br>Cornstarch – 2 tbsp, Sugar – 2 tbsp</span>
  <span class="tiny dark" style="left:8px;top:207px;font-size:1.9px">For the Whipped Cream Frosting</span>
  <span class="tiny" style="left:8px;top:210px;font-size:1.8px;line-height:2.6px">Heavy whipping cream – 300 ml, chilled<br>Powdered sugar – 80 g, Vanilla extract – 1 tsp</span>
  <span class="tiny dark" style="left:8px;top:217px;font-size:1.9px">For Decoration</span>
  <span class="tiny" style="left:8px;top:220px;font-size:1.8px;line-height:2.6px">Chocolate shavings – 100 g<br>Maraschino cherries – 10-12</span>

  <div style="left:3px;right:3px;top:260px;height:202px;background:var(--white);border-radius:2px;border:.4px solid var(--line)"></div>
  <span class="h" style="left:8px;top:264px;font-size:2.7px">Recipe Steps</span>
  <span class="tiny" style="right:9px;top:264px;color:var(--orange);font-size:1.9px">Saved</span>
  <div role="img" aria-label="Sponge step photo" style="left:8px;top:273px;width:22px;height:22px;border-radius:2px;background:linear-gradient(135deg,#eadbd3,#6b3a34)"></div>
  <span class="tiny green" style="left:33px;top:272px;font-size:2px">Step 1: Prepare the Chocolate Sponge</span>
  <span class="tiny" style="left:33px;top:276px;font-size:1.7px;line-height:2.5px">1. Preheat oven, grease two pans.<br>2. Sift flour, cocoa and salt.<br>3. Beat eggs and sugar, add milk.<br>4. Fold in dry mix, add water.<br>5. Bake 30-35 minutes, cool.</span>
  <div role="img" aria-label="Cherry step photo" style="left:8px;top:319px;width:22px;height:22px;border-radius:2px;background:linear-gradient(135deg,#f1e4dc,#b3262d)"></div>
  <span class="tiny green" style="left:33px;top:318px;font-size:2px">Step 2: Make the Cherry Filling</span>
  <span class="tiny" style="left:33px;top:322px;font-size:1.7px;line-height:2.5px">1. Heat cherries with syrup.<br>2. Add cornstarch mix, stir.<br>3. Cook until thick, cool.</span>
  <div role="img" aria-label="Cream step photo" style="left:8px;top:346px;width:22px;height:22px;border-radius:2px;background:linear-gradient(135deg,#f3e3d3,#8a4a2a)"></div>
  <span class="tiny green" style="left:33px;top:345px;font-size:2px">Step 3: Whip the Cream</span>
  <span class="tiny" style="left:33px;top:349px;font-size:1.7px;line-height:2.5px">1. Chill bowl and beaters.<br>2. Beat cream, add sugar.<br>3. Whip to stiff peaks.</span>
  <div role="img" aria-label="Assembly step photo" style="left:8px;top:373px;width:22px;height:22px;border-radius:2px;background:linear-gradient(135deg,#d9cfc9,#3a2a28)"></div>
  <span class="tiny green" style="left:33px;top:372px;font-size:2px">Step 4: Assemble the Cake</span>
  <span class="tiny" style="left:33px;top:376px;font-size:1.7px;line-height:2.5px">1. Slice cakes into layers.<br>2. Brush with cherry syrup.<br>3. Add cream and cherries.<br>4. Repeat with other layers.</span>
  <div role="img" aria-label="Finished cake step photo" style="left:8px;top:408px;width:22px;height:22px;border-radius:2px;background:linear-gradient(135deg,#f6dfe0,#c06070)"></div>
  <span class="tiny green" style="left:33px;top:407px;font-size:2px">Step 5: Frost and Decorate</span>
  <span class="tiny" style="left:33px;top:411px;font-size:1.7px;line-height:2.5px">1. Cover cake with cream.<br>2. Press on chocolate shavings.<br>3. Top with cream and cherries.</span>

  <div class="thumb" role="img" aria-label="Chef profile photo" style="left:8px;top:480px;width:8px;height:8px;background:#7a6e66"></div>
  <span class="tiny dark" style="left:19px;top:482px">Rate our Chef</span>
  <span class="tiny" style="right:8px;top:481px">★★★★★</span>
  <span class="tiny green" style="left:8px;top:494px">Give your review</span>
  <div style="left:8px;right:8px;top:500px;height:28px;border:.4px solid var(--line);border-radius:1.5px"></div>
  <span class="tiny" style="left:11px;top:502px;font-size:1.8px">Write your review</span>
  <span class="tiny" style="right:11px;top:524px;font-size:1.6px">0/500</span>
  <span class="chip ghost" style="left:58px;top:532px;width:14px">Delete</span>
  <span class="chip" style="left:76px;top:532px;width:14px">Post</span>

  <div class="thumb" role="img" aria-label="Chef profile photo" style="left:8px;top:557px;width:8px;height:8px;background:#7a6e66"></div>
  <span class="tiny dark" style="left:19px;top:559px">Explore other dishes</span>
  <div class="dish" role="img" aria-label="Rolls dish" style="left:9px;top:573px;background:#f2a23a"></div>
  <div class="dish" role="img" aria-label="Pizza dish" style="left:30px;top:573px;background:#e5c9a0"></div>
  <div class="dish" role="img" aria-label="Noodles dish" style="left:51px;top:573px;background:#d8412f"></div>
  <div class="dish" role="img" aria-label="Cake dish" style="left:72px;top:573px;background:#e8c0c8"></div>
  <span class="tiny dark" style="left:10px;top:585px;font-size:1.7px">Rolls</span>
  <span class="tiny dark" style="left:31px;top:585px;font-size:1.7px">Pizza</span>
  <span class="tiny dark" style="left:51px;top:585px;font-size:1.7px">Noodles</span>
  <span class="tiny dark" style="left:74px;top:585px;font-size:1.7px">Cake</span>
</div>

</body>
</html>
```